Velmora.net - A website for sensual content creators (like PeakPatron)

Web Design Contest for Velmora.net
Overview: Velmora.net is set to be the next big name in the world of content creation, blending a modern social media platform with exclusive 18+ paid content. Unlike competitors like PeakPatron and Subvio, Velmora.net will offer a unique and intuitive user experience that stands out for its clean, modern design and effortless usability.

Platform Features:

Dual Content Modes: Velmora.net offers a mix of safe-for-work social media content, alongside private and paid media for 18+ users.
Content Creators Hub: A space for creators to share sensual, engaging, and private media, with opportunities to grow their fanbase and monetize their work.
Live Streaming & Messaging: Creators can connect with their audience through live streams and private messages (both live and asynchronous).
Community Building: Users can explore content, interact with creators, and engage in a rich social experience.
Design Goals:

Front Page (Logged Out): The landing page should captivate new visitors while clearly outlining what Velmora.net offers. A balance of intrigue and professionalism is key here. The goal is to attract both content creators and consumers, showcasing the platform's potential in an elegant and tasteful manner. Minimalistic yet bold, the design should avoid overwhelming visitors with too much information but leave a lasting impression. The color palette, fonts, and imagery should feel fresh, clean, and inviting.

Logged-In Dashboard: This design should prioritize easy navigation for creators and users alike. Think of a sleek, customizable dashboard where everything is at your fingertips—from content creation tools to messaging, analytics, and payment settings. The user experience should feel smooth and modern without sacrificing functionality. Visual clarity and an emphasis on user empowerment are crucial.

Messaging Page (Live Chat): The live chat feature needs to feel dynamic and interactive, with a design that makes real-time conversations feel personal and engaging. Consider features like reactions, media sharing, and notifications—all wrapped up in a sleek interface. The layout should encourage interaction while remaining clean and distraction-free.

Normal Chat: For asynchronous messaging, aim for a layout that balances simplicity and depth. Users should be able to easily track their conversations, search through chats, and engage in a natural flow. Think of it as a hybrid between social messaging apps and content creator tools, offering the best of both worlds in a clutter-free space.

Style & Aesthetic: We’re looking for a design that’s modern, sleek, and minimal but still leaves room for personality. It should feel fresh and distinct from the competition. Focus on UX/UI that feels unique to Velmora.net, ensuring that navigation is effortless and the platform is approachable to both creators and consumers. Avoid the heavy, cluttered feel of other platforms—this needs to be light, easy to use, and beautifully crafted. Clean lines, innovative layout, and a user-first experience are key here.

Target Market(s)

Women

Industry/Entity Type

Adult/Content Creation

Number of Pages Required

5+ page

Colors

Designer to choose only greyscale colors for use in the design.

Requirements
Must have
• Front page, logged in page (with feed/etc), streaming page (1-1), and chat page.
Nice to have
• I just want something unique that stands out. I do not want a 1:1 copy of PeakPatron or Subvoi. The feel of the site should be classy but mordern and sensual. We want to attract people and avoid looking like a porn site (which we're not)

```html
<!DOCTYPE html>
<html lang="en">
<head>
<meta charset="utf-8">
<title>Velmora – Creator Dashboard</title>
<link href="https://fonts.googleapis.com/css2?family=Montserrat:wght@400;500;600;700&display=swap" rel="stylesheet">
<style>
:root{
  --brand:#2e2e2e;
  --brand-soft:#d4d4d4;
  --brand-tint:#ececec;
  --head-a:#1c1c1c;
  --head-b:#2f2f2f;
  --head-c:#454545;
  --nav-active:rgba(255,255,255,.18);
  --panel:#f3f3f3;
  --card:#fdfdfd;
  --ink:#3c3c3c;
  --ink-soft:#7a7a7a;
  --line:#e6e6e6;
  --up:#4a4a4a;
  --up-bg:#e4e4e4;
}
*{box-sizing:border-box;margin:0;padding:0}
html,body{width:1200px;height:900px;overflow:hidden}
body{font-family:"Montserrat",sans-serif;color:var(--ink);background:linear-gradient(120deg,var(--head-a) 0%,var(--head-b) 50%,var(--head-c) 100%);}
.app{width:1200px;height:900px;display:flex;flex-direction:column}
.topbar{height:68px;display:flex;align-items:center;padding:0 24px;position:relative}
.brand{display:flex;align-items:center;gap:8px;color:#fff;font-weight:600;font-size:24px;letter-spacing:-.3px}
.brand-dot{width:10px;height:10px;border-radius:50%;background:#fff}
.main-nav{position:absolute;left:50%;transform:translateX(-50%);display:flex;gap:14px}
.nav-item{display:flex;align-items:center;gap:8px;height:40px;padding:0 26px;border-radius:20px;color:#fff;font-weight:600;font-size:12px}
.nav-item svg{width:12px;height:12px}
.nav-item.is-active{background:var(--nav-active)}
.top-actions{margin-left:auto;display:flex;gap:12px}
.round-btn{width:32px;height:32px;border-radius:50%;background:rgba(255,255,255,.16);display:flex;align-items:center;justify-content:center}
.round-btn svg{width:13px;height:13px}
.avatar{width:32px;height:32px;border-radius:50%;background:linear-gradient(135deg,#6a6a6a,#a8a8a8);border:2px solid rgba(255,255,255,.6)}
.panel{flex:1;margin:0 19px 20px;background:var(--panel);border-radius:18px;padding:19px;overflow:hidden;display:flex;flex-direction:column}
.tabs{display:flex;align-items:center;gap:26px;margin-bottom:20px}
.tab{font-size:12px;font-weight:600;color:var(--ink-soft)}
.tab.is-active{display:flex;align-items:center;gap:8px;background:var(--brand);color:#fff;height:40px;padding:0 26px;border-radius:20px}
.tab.is-active svg{width:12px;height:12px}
.grid{flex:1;display:grid;grid-template-columns:1fr 318px;gap:20px;min-height:0}
.col-main{display:flex;flex-direction:column;gap:20px;min-height:0}
.col-side{display:flex;flex-direction:column;gap:20px}
.card{background:var(--card);border-radius:14px;box-shadow:0 4px 18px rgba(0,0,0,.05)}
.stats{display:grid;grid-template-columns:repeat(4,1fr);gap:20px}
.stat{height:90px;padding:18px 19px}
.stat-label{font-size:9.5px;color:var(--ink-soft)}
.stat-value{font-size:19px;font-weight:700;margin-top:14px}
.metric{padding:19px 19px 0}
.metric-head{display:flex;gap:12px;align-items:flex-start;position:relative}
.metric-icon{width:32px;height:32px;border-radius:50%;background:var(--brand-tint);display:flex;align-items:center;justify-content:center;color:var(--brand);font-size:12px;font-weight:500}
.metric-title{font-size:11.5px;font-weight:600;margin-top:2px}
.metric-dates{font-size:9px;color:var(--ink-soft);margin-top:6px}
.metric-total{display:flex;align-items:center;gap:12px;margin-top:26px}
.metric-amount{font-size:19px;color:var(--brand);font-weight:500}
.trend{display:flex;align-items:center;gap:6px;font-size:9px;color:var(--ink-soft)}
.trend-dot{width:14px;height:14px;border-radius:50%;background:var(--up-bg);display:flex;align-items:center;justify-content:center}
.trend-dot svg{width:8px;height:8px}
.metric-chart{position:absolute;right:0;top:0;width:484px;height:92px;overflow:visible}
.breakdown{border-top:1px solid var(--line);margin-top:26px;padding:22px 0 20px;display:grid;grid-template-columns:repeat(4,1fr);row-gap:20px}
.cell{padding-right:10px;border-right:1px solid var(--line)}
.cell:nth-child(4n){border-right:none}
.cell+.cell:not(:nth-child(4n+1)){padding-left:70px}
.cell-label{font-size:9.5px;color:var(--ink-soft)}
.cell-value{font-size:11.5px;font-weight:600;margin-top:8px}
.metric-tx{flex:1;min-height:0;overflow:hidden}
.time-card{padding:20px 19px;height:284px}
.side-title{font-size:11.5px;font-weight:600}
.donut-wrap{position:relative;width:146px;height:146px;margin:22px auto 0}
.donut-label{position:absolute;inset:0;display:flex;align-items:center;justify-content:center;font-size:11px;font-weight:600}
.legend{display:flex;justify-content:center;gap:26px;margin-top:26px}
.legend-hrs{font-size:11px;font-weight:600}
.legend-name{display:flex;align-items:center;gap:7px;font-size:11px;color:var(--ink-soft);margin-top:9px}
.legend-dot{width:9px;height:9px;border-radius:50%}
.analyze-card{flex:1;padding:20px 19px;display:flex;flex-direction:column}
.analyze-text{font-size:11px;color:var(--ink-soft);line-height:1.45;margin-top:9px}
.select{margin-top:26px;height:40px;border:1px solid var(--line);border-radius:8px;display:flex;align-items:center;gap:9px;padding:0 14px;font-size:11px;color:var(--ink-soft)}
.select svg{width:13px;height:13px}
.select .caret{margin-left:auto;width:10px}
.btn-primary{margin-top:auto;height:30px;border-radius:15px;background:var(--brand);color:#fff;font-size:9.5px;font-weight:600;display:flex;align-items:center;justify-content:center}
</style>
</head>
<body>
<div class="app">
  <header class="topbar">
    <div class="brand"><span>Velmora</span><span class="brand-dot"></span></div>
    <nav class="main-nav">
      <div class="nav-item is-active"><svg viewBox="0 0 12 12" fill="none" stroke="#fff" stroke-width="1.2"><rect x="1" y="1" width="4" height="4" rx="1"/><rect x="7" y="1" width="4" height="4" rx="1"/><rect x="1" y="7" width="4" height="4" rx="1"/><rect x="7" y="7" width="4" height="4" rx="1"/></svg>Overview</div>
      <div class="nav-item"><svg viewBox="0 0 12 12" fill="none" stroke="#fff" stroke-width="1.2"><rect x="1" y="2" width="10" height="7" rx="1"/><path d="M5 4l2.5 1.5L5 7z" fill="#fff" stroke="none"/><path d="M3 11h6"/></svg>Content</div>
      <div class="nav-item"><svg viewBox="0 0 12 12" fill="none" stroke="#fff" stroke-width="1.2"><circle cx="6" cy="6" r="5"/><path d="M7.5 4.3c-.4-.5-1-.7-1.6-.6-.8.1-1.2.6-1 1.1.3.9 2.7.6 2.8 1.7.1.7-.6 1.2-1.5 1.2-.6 0-1.2-.3-1.5-.8M6 3v6"/></svg>Monetization</div>
      <div class="nav-item"><svg viewBox="0 0 12 12" fill="none" stroke="#fff" stroke-width="1.2"><path d="M6 1.2a4.8 4.8 0 0 0-4.2 7.1L1.2 10.8l2.5-.6A4.8 4.8 0 1 0 6 1.2z"/><circle cx="4" cy="6" r=".5" fill="#fff"/><circle cx="6" cy="6" r=".5" fill="#fff"/><circle cx="8" cy="6" r=".5" fill="#fff"/></svg>Messaging</div>
    </nav>
    <div class="top-actions">
      <div class="round-btn"><svg viewBox="0 0 14 14" fill="none" stroke="#fff" stroke-width="1.4"><circle cx="6" cy="6" r="4.5"/><path d="M9.5 9.5L13 13"/></svg></div>
      <div class="round-btn"><svg viewBox="0 0 14 14" fill="none" stroke="#fff" stroke-width="1.3"><path d="M3 10V6.5a4 4 0 0 1 8 0V10l1 1.2H2zM5.8 12.6h2.4"/></svg></div>
      <div class="avatar" role="img" aria-label="Creator profile photo"></div>
    </div>
  </header>

  <main class="panel">
    <div class="tabs">
      <div class="tab is-active"><svg viewBox="0 0 12 12" fill="none" stroke="#fff" stroke-width="1.2"><path d="M1 11h10M3 11V6M6 11V2M9 11V5"/></svg>Overview of today’s activity</div>
      <div class="tab">Rate analysis</div>
      <div class="tab">Referrals</div>
    </div>

    <div class="grid">
      <section class="col-main">
        <div class="stats">
          <div class="card stat"><div class="stat-label">New Messages</div><div class="stat-value">5 unread</div></div>
          <div class="card stat"><div class="stat-label">New Followers</div><div class="stat-value">+12</div></div>
          <div class="card stat"><div class="stat-label">Earnings Today</div><div class="stat-value">$450</div></div>
          <div class="card stat"><div class="stat-label">Upcoming Scheduled Posts</div><div class="stat-value">2</div></div>
        </div>

        <article class="card metric">
          <div class="metric-head">
            <div class="metric-icon">$</div>
            <div>
              <div class="metric-title">Total revenue</div>
              <div class="metric-dates">14 July 2024 - 18 July 2024</div>
            </div>
            <svg class="metric-chart" viewBox="0 0 484 92" preserveAspectRatio="none">
              <defs><linearGradient id="fillRev" x1="0" y1="0" x2="0" y2="1"><stop offset="0" stop-color="#2e2e2e" stop-opacity=".08"/><stop offset="1" stop-color="#2e2e2e" stop-opacity="0"/></linearGradient></defs>
              <path d="M0 86 C20 86 30 86 40 85 S60 79 75 78 S100 76 115 75 S140 72 155 69 S175 66 190 65 S210 65 220 64 S240 64 250 60 S270 51 285 50 S305 50 315 47 S335 38 350 37 S375 36 385 35 S400 33 410 33 S425 26 435 25 S455 20 465 17 S476 8 480 6 L480 92 L0 92Z" fill="url(#fillRev)"/>
              <path d="M0 86 C20 86 30 86 40 85 S60 79 75 78 S100 76 115 75 S140 72 155 69 S175 66 190 65 S210 65 220 64 S240 64 250 60 S270 51 285 50 S305 50 315 47 S335 38 350 37 S375 36 385 35 S400 33 410 33 S425 26 435 25 S455 20 465 17 S476 8 480 6" fill="none" stroke="#2e2e2e" stroke-width="1.4"/>
              <circle cx="480" cy="6" r="3" fill="#2e2e2e"/>
            </svg>
          </div>
          <div class="metric-total">
            <span class="metric-amount">$235,175.00</span>
            <span class="trend"><span class="trend-dot"><svg viewBox="0 0 8 8" fill="none" stroke="#4a4a4a" stroke-width="1.2"><path d="M4 7V1M1.5 3.5L4 1l2.5 2.5"/></svg></span>24.21%</span>
          </div>
          <div class="breakdown">
            <div class="cell"><div class="cell-label">Paid streams</div><div class="cell-value">$5,208.00</div></div>
            <div class="cell"><div class="cell-label">1-on-1 streams</div><div class="cell-value">$5,829.00</div></div>
            <div class="cell"><div class="cell-label">Media</div><div class="cell-value">$8,624.00</div></div>
            <div class="cell"><div class="cell-label">Calls</div><div class="cell-value">$825.00</div></div>
            <div class="cell"><div class="cell-label">Private message</div><div class="cell-value">$375.00</div></div>
            <div class="cell"><div class="cell-label">Tips</div><div class="cell-value">$4,252.00</div></div>
            <div class="cell"><div class="cell-label">Collabs</div><div class="cell-value">$9,902.00</div></div>
            <div class="cell"><div class="cell-label">Offers</div><div class="cell-value">$2,779.00</div></div>
            <div class="cell"><div class="cell-label">Ads</div><div class="cell-value">$1,942.00</div></div>
            <div class="cell"><div class="cell-label">Referrals</div><div class="cell-value">$9,615.00</div></div>
          </div>
        </article>

        <article class="card metric metric-tx">
          <div class="metric-head">
            <div class="metric-icon"><svg width="11" height="11" viewBox="0 0 12 12" fill="none" stroke="#2e2e2e" stroke-width="1.1"><rect x="1" y="4" width="8" height="6" rx="1"/><path d="M3 2h7a1 1 0 0 1 1 1v5"/></svg></div>
            <div>
              <div class="metric-title">Total transactions</div>
              <div class="metric-dates">14 July 2024 - 18 July 2024</div>
            </div>
            <svg class="metric-chart" viewBox="0 0 484 92" preserveAspectRatio="none">
              <defs><linearGradient id="fillTx" x1="0" y1="0" x2="0" y2="1"><stop offset="0" stop-color="#2e2e2e" stop-opacity=".08"/><stop offset="1" stop-color="#2e2e2e" stop-opacity="0"/></linearGradient></defs>
              <path d="M0 86 C20 86 30 86 40 85 C55 84 60 79 75 78 C90 77 100 76 115 75 C130 74 140 72 155 69 C170 66 178 65 190 65 C205 65 212 64 220 63 C235 62 242 61 250 58 C262 53 272 50 285 50 C300 50 308 49 315 46 C328 40 338 33 345 34 C352 35 353 48 357 46 C360 40 362 36 375 35 C390 34 398 33 405 33 C412 33 414 45 419 44 C423 42 425 33 437 29 C448 26 452 26 460 22 C466 19 470 18 472 20 C474 22 474 36 476 36 C478 36 478 12 479 10 C480 8 482 16 480 24 L480 92 L0 92Z" fill="url(#fillTx)"/>
              <path d="M0 86 C20 86 30 86 40 85 C55 84 60 79 75 78 C90 77 100 76 115 75 C130 74 140 72 155 69 C170 66 178 65 190 65 C205 65 212 64 220 63 C235 62 242 61 250 58 C262 53 272 50 285 50 C300 50 308 49 315 46 C328 40 338 33 345 34 C352 35 353 48 357 46 C360 40 362 36 375 35 C390 34 398 33 405 33 C412 33 414 45 419 44 C423 42 425 33 437 29 C448 26 452 26 458 23 C462 21 464 20 465 22 C466 26 466 38 468 38 C471 38 471 8 474 8 C477 8 478 18 480 24" fill="none" stroke="#2e2e2e" stroke-width="1.4"/>
              <circle cx="480" cy="24" r="3" fill="#2e2e2e"/>
            </svg>
          </div>
          <div class="metric-total">
            <span class="metric-amount">$35,175.00</span>
            <span class="trend"><span class="trend-dot"><svg viewBox="0 0 8 8" fill="none" stroke="#4a4a4a" stroke-width="1.2"><path d="M4 7V1M1.5 3.5L4 1l2.5 2.5"/></svg></span>14.21%</span>
          </div>
          <div class="breakdown">
            <div class="cell"><div class="cell-label">Paid streams</div></div>
            <div class="cell"><div class="cell-label">Media</div></div>
            <div class="cell"><div class="cell-label">Calls</div></div>
            <div class="cell"><div class="cell-label">Private message</div></div>
          </div>
        </article>
      </section>

      <aside class="col-side">
        <div class="card time-card">
          <div class="side-title">Time online</div>
          <div class="donut-wrap">
            <svg width="146" height="146" viewBox="0 0 146 146">
              <circle cx="73" cy="73" r="63" fill="none" stroke="#d4d4d4" stroke-width="20"/>
              <circle cx="73" cy="73" r="63" fill="none" stroke="#2e2e2e" stroke-width="20" stroke-dasharray="194 396" transform="rotate(-90 73 73)"/>
            </svg>
            <div class="donut-label">94hrs</div>
          </div>
          <div class="legend">
            <div><div class="legend-hrs">46hrs</div><div class="legend-name"><span class="legend-dot" style="background:var(--brand)"></span>Desktop</div></div>
            <div><div class="legend-hrs">48hrs</div><div class="legend-name"><span class="legend-dot" style="background:var(--brand-soft)"></span>Mobile</div></div>
          </div>
        </div>

        <div class="card analyze-card">
          <div class="side-title">Analyze report</div>
          <p class="analyze-text">This help you understand and choose your optimal rate and when to be online.</p>
          <div class="select">
            <svg viewBox="0 0 14 14" fill="none" stroke="#7a7a7a" stroke-width="1.1"><rect x="1" y="3.5" width="12" height="8.5" rx="1.5"/><circle cx="7" cy="7.7" r="2.2"/><path d="M5 3.5l1-1.5h2l1 1.5"/></svg>
            Live streams
            <svg class="caret" viewBox="0 0 10 6" fill="none" stroke="#2e2e2e" stroke-width="1.3"><path d="M1 1l4 4 4-4z"/></svg>
          </div>
          <div class="btn-primary">Analyze</div>
        </div>
      </aside>
    </div>
  </main>
</div>
</body>
</html>
```